依頼詳細
バイクで周辺のニュータウンに配布を考えています。
量販店よりもかなり安いので、安いとわかるようなチラシに仕上げたいです。
また、片面にウォーターサーバーのサブスクの内容を入れてます。
デザインは近いものでイラストを考えています。
記載項目
社名・電話番号・料金プラン
エアコンの取付・取外しをお得にできます。
エアコン基本設置4m 11,000円~
エアコン基本外し 4,000円(2台台以上)
(外し単品は6,000円)
価格は税込み
サイズ
A5
ページ数
片面
希望イメージ
シンプル 複雑
単色 カラフル
暗い 明るい
日常 高級
遊び心 厳粛
未来的 伝統的
女性的 男性的
希望する色
黄・オレンジ系
納品ファイル
• イラストレーター形式 (.ai)
補足説明
■ 選んだ理由

こちらで想定していたのと全然違う構成に感銘を受けました。
かなり手直しが必要ですが、こちらの路線でチラシを作成しようと思います。

■ 提案者全員のお礼・コメント

今回はたくさんのご応募をいただき大変感謝しております。
たくさんのパターンがあり感動しています。
また、同じような応募をしますのでその際はよろしくお願いいたします

```html
<!DOCTYPE html>
<html lang="ja">
<head>
<meta charset="UTF-8">
<title>エアコンの取付・取外し チラシ</title>
<link href="https://fonts.googleapis.com/css2?family=M+PLUS+Rounded+1c:wght@700;800;900&family=Noto+Sans+JP:wght@500;700;900&display=swap" rel="stylesheet">
<style>
:root{
  --yellow:#f9c51c;
  --orange:#f08300;
  --navy:#1f2a44;
  --ink:#2b2b2b;
  --white:#ffffff;
  --gray:#b9b9b9;
  --muted:#555555;
  --illust-a:#f6d35a;
  --illust-b:#e9b524;
}
*{margin:0;padding:0;box-sizing:border-box}
html,body{width:848px;height:1200px;overflow:hidden;background:var(--yellow)}
body{font-family:"Noto Sans JP",sans-serif;color:var(--ink)}
.flyer{position:relative;width:848px;height:1200px;background:var(--yellow);overflow:hidden}

.headline-pill{
  position:absolute;left:124px;top:32px;width:600px;height:82px;
  background:var(--white);border-radius:41px;
  display:flex;align-items:center;justify-content:center;
  font-family:"M PLUS Rounded 1c",sans-serif;font-weight:800;font-size:46px;color:var(--navy);
  white-space:nowrap;
}
.headline-pill .accent{color:var(--orange)}

.main-title{
  position:absolute;left:0;top:122px;width:848px;text-align:center;white-space:nowrap;
  font-family:"M PLUS Rounded 1c",sans-serif;font-weight:900;font-size:100px;line-height:1.15;
  color:var(--orange);
  -webkit-text-stroke:14px var(--white);paint-order:stroke fill;
}
.main-title .small{font-size:74px}

.scene-illustration{
  position:absolute;left:110px;top:268px;width:640px;height:452px;
  border-radius:24px;
  background:linear-gradient(160deg,var(--illust-a),var(--illust-b));
}

.callout{
  position:absolute;writing-mode:vertical-rl;text-orientation:upright;
  font-family:"Noto Sans JP",sans-serif;font-weight:700;font-size:28px;line-height:1;
  color:var(--navy);letter-spacing:3px;white-space:nowrap;
}
.callout--left{left:36px;top:330px}
.callout--right{right:36px;top:330px}

.price-panel{
  position:absolute;left:28px;top:730px;width:792px;height:325px;
  background:var(--white);border:6px solid var(--orange);border-radius:10px;
}
.price-tag{
  position:absolute;left:18px;top:16px;width:140px;height:140px;
  background:var(--orange);color:var(--white);border-radius:6px;
  font-family:"M PLUS Rounded 1c",sans-serif;font-weight:900;font-size:48px;line-height:1.1;
  display:flex;flex-direction:column;align-items:center;justify-content:center;
}
.tax-note{position:absolute;left:18px;top:266px;font-size:15px;color:var(--muted)}

.price-row{position:absolute;left:185px;display:flex;align-items:center}
.price-row--install{top:26px}
.price-row--removal{top:140px}
.price-label{font-weight:700;font-size:28px;line-height:1.25;color:var(--ink);width:190px;white-space:nowrap}
.price-label .sub{display:block;font-size:28px}
.price-label .sub--small{font-size:20px;font-weight:500}
.price-amount{
  font-family:"M PLUS Rounded 1c",sans-serif;font-weight:900;font-size:80px;color:var(--orange);line-height:1;white-space:nowrap;
}
.price-amount .unit{font-size:38px;font-weight:800}
.single-note{position:absolute;right:24px;top:258px;font-weight:700;font-size:26px;color:var(--ink);white-space:nowrap}

.contact-band{
  position:absolute;left:0;top:1070px;width:848px;height:130px;background:var(--white);
}
.logo-mark{position:absolute;left:36px;top:22px;width:110px;height:86px;background:var(--gray)}
.company-name{position:absolute;left:188px;top:16px;font-weight:700;font-size:26px;color:var(--ink)}
.phone{
  position:absolute;left:188px;top:54px;display:flex;align-items:center;gap:14px;white-space:nowrap;
  font-family:"M PLUS Rounded 1c",sans-serif;font-weight:800;font-size:60px;color:var(--orange);line-height:1;
}
.phone svg{width:56px;height:56px}
</style>
</head>
<body>
<div class="flyer">
  <div class="headline-pill">エアコンの<span class="accent">取付・取外し</span></div>
  <h1 class="main-title">お得<span class="small">に</span>できます。</h1>

  <div class="scene-illustration" role="img" aria-label="作業服の男女スタッフが室内機と室外機を手で示すイラスト"></div>
  <p class="callout callout--left">お問合せください。</p>
  <p class="callout callout--right">お気軽に</p>

  <section class="price-panel">
    <div class="price-tag"><span>エア</span><span>コン</span></div>
    <p class="tax-note">※価格は税込みです。</p>
    <div class="price-row price-row--install">
      <p class="price-label">基本<span class="sub">取付4m</span></p>
      <p class="price-amount">11,000<span class="unit">円〜</span></p>
    </div>
    <div class="price-row price-row--removal">
      <p class="price-label">基本取外し<span class="sub sub--small">(2台以上の場合)</span></p>
      <p class="price-amount">4,000<span class="unit">円〜</span></p>
    </div>
    <p class="single-note">取外し1台の場合は6,000円</p>
  </section>

  <footer class="contact-band">
    <div class="logo-mark"></div>
    <p class="company-name">株式会社ヒナタ</p>
    <p class="phone">
      <svg viewBox="0 0 58 58" aria-hidden="true">
        <circle cx="29" cy="29" r="29" fill="var(--orange)"/>
        <path d="M20 15c2 0 3 1 4 3l2 5c0 2-1 3-2 4 1 3 4 6 7 7 1-1 2-2 4-2l5 2c2 1 3 2 3 4 0 3-3 6-6 6-11 0-21-10-21-21 0-3 3-6 4-8z" fill="var(--white)"/>
      </svg>
      0120-381-276
    </p>
  </footer>
</div>
</body>
</html>
```